Art Exhibit Invitation Design

This is an exhibit invitation for a three-artist show. The final postcard will be 6X9 and placed in an envelope of 6 1/2 by 9 1/2. I have placed two logos we use (although the logo color is pink, it is possible that the color can be changed. The artists are Marla Bennick, Lynette Paulsen, and Rosalind Metcalf. The corresponding images are Lynette (apple tree), Rosalind (green celadon), and Marla (Poppies). The show runs July 8 - Aug 25. The opening Reception is Saturday, July 8 from 3-5pm. I would like this done in Adobe InDesign. Since the postcard is being put in an envelope, information about the exhibit can be put on the back (no return address or stamp will be needed) .
The Quimby Gallery is located at 2813 E Fernwood Ave, Yakima WA 98907. our phone is (509) 555-0193.
The exhibit title is Quiet Harvest.
Lynette works in Pastel, Marla is a painter, and Rosalnd is a ceramicist.

```html
<!DOCTYPE html>
<html lang="en">
<head>
<meta charset="utf-8">
<title>Quiet Harvest – Exhibit Invitation</title>
<link rel="stylesheet" href="https://fonts.googleapis.com/css2?family=Abel&family=Oswald:wght@600&display=swap">
<style>
  :root {
    --page: #ffffff;
    --pink: #e8137f;
    --ink: #231f20;
    --cream: #fdf8ec;
    --white-soft: rgba(255,255,255,0.55);
    --white-faint: rgba(255,255,255,0.3);
  }
  * { margin: 0; padding: 0; box-sizing: border-box; }
  html, body { width: 1200px; height: 461px; overflow: hidden; background: var(--page); }
  .invite { position: relative; width: 1200px; height: 461px; font-family: "Abel", sans-serif; }

  /* Front: three artwork strips */
  .strip { position: absolute; top: 18px; height: 425px; overflow: hidden; }
  .strip--pastel { left: 23px; width: 185px;
    background: linear-gradient(170deg, #f1d3cf 0%, #d9a7a3 25%, #9db27c 55%, #6f8f4f 80%, #8aa05e 100%); }
  .strip--ceramic { left: 211px; width: 183px;
    background: radial-gradient(circle at 50% 55%, #d9e6df 0%, #c3d6cf 45%, #a9c2ba 100%); }
  .strip--painting { left: 397px; width: 181px;
    background: linear-gradient(160deg, #d8c4a0 0%, #e06a38 28%, #c63b1f 45%, #e3b55b 62%, #6f8e4e 82%, #3f5e3a 100%); }
  .strip__artist { position: absolute; bottom: 6px; left: 6px; color: #fff; font-size: 16px; letter-spacing: 0.5px; white-space: nowrap; }

  .title-overlay { position: absolute; left: 23px; top: 18px; width: 555px; height: 425px; pointer-events: none; }
  .title-overlay__main { position: absolute; left: 0; width: 555px; top: 138px; text-align: center;
    font-family: "Oswald", sans-serif; font-weight: 600; font-size: 176px; line-height: 1; color: var(--white-soft); letter-spacing: 8px; }
  .title-overlay__sub { position: absolute; left: 0; width: 555px; top: 196px; text-align: center;
    font-family: "Oswald", sans-serif; font-weight: 600; font-size: 96px; line-height: 1; color: transparent;
    -webkit-text-stroke: 2px var(--white-faint); letter-spacing: 4px; }

  .brand { position: absolute; display: flex; flex-direction: column; align-items: center; gap: 6px; color: var(--pink); }
  .brand__dot { width: 54px; height: 54px; border-radius: 50%; background: var(--pink); }
  .brand__name { font-size: 15px; letter-spacing: 1px; }
  .brand--front { left: 262px; top: 40px; }

  /* Back: postcard */
  .postcard { position: absolute; left: 601px; top: 18px; width: 584px; height: 421px;
    background: repeating-linear-gradient(135deg, var(--pink) 0 14px, #fff 14px 26px, var(--ink) 26px 40px, #fff 40px 52px);
    box-shadow: 3px 4px 8px rgba(0,0,0,0.25); }
  .postcard__face { position: absolute; inset: 15px; background: var(--cream); }
  .postcard__divider { position: absolute; left: 261px; top: 32px; width: 2px; height: 150px; background: var(--ink); }

  .event { position: absolute; left: 24px; top: 44px; width: 226px; }
  .event__kicker { color: var(--pink); font-size: 21px; letter-spacing: 1px; }
  .event__title { color: var(--ink); font-size: 34px; font-weight: 400; letter-spacing: 0.5px; line-height: 1.25; margin-top: 4px; white-space: nowrap; }
  .event__date { color: var(--pink); font-size: 21px; letter-spacing: 1.5px; margin-top: 8px; }

  .artists { position: absolute; left: 26px; top: 200px; list-style: none; }
  .artists__item { width: 212px; font-size: 21px; letter-spacing: 0.5px; color: var(--ink);
    border-bottom: 1.5px solid var(--ink); padding-bottom: 2px; margin-bottom: 22px; white-space: nowrap; }

  .brand--back { left: 440px; top: 28px; }
  .brand--back .brand__name { color: var(--ink); font-weight: 400; }
  .brand--back .brand__dot { width: 58px; height: 58px; }

  .contact { position: absolute; right: 40px; top: 132px; text-align: right; font-size: 15px; line-height: 1.5; color: var(--ink); font-style: normal; }
</style>
</head>
<body>
<main class="invite">
  <section class="front">
    <div class="strip strip--pastel" role="img" aria-label="Pastel of a flowering apple tree by Lynette Paulsen">
      <span class="strip__artist">LYNETTE PAULSEN</span>
    </div>
    <div class="strip strip--ceramic" role="img" aria-label="Green celadon ceramic with carved relief by Rosalind Metcalf">
      <span class="strip__artist">ROSALIND METCALF</span>
    </div>
    <div class="strip strip--painting" role="img" aria-label="Painting of red poppies by Marla Bennick">
      <span class="strip__artist">MARLA BENNICK</span>
    </div>

    <div class="title-overlay" aria-hidden="true">
      <span class="title-overlay__sub">HARVEST</span>
      <span class="title-overlay__main">QUIET</span>
    </div>

    <div class="brand brand--front">
      <span class="brand__dot"></span>
      <span class="brand__name">QUIMBY</span>
    </div>
  </section>

  <section class="postcard">
    <div class="postcard__face">
      <div class="event">
        <p class="event__kicker">Grand Opening</p>
        <h1 class="event__title">QUIET HARVEST</h1>
        <p class="event__date">July 8 &nbsp;/&nbsp; 3-5pm</p>
      </div>
      <span class="postcard__divider"></span>

      <ul class="artists">
        <li class="artists__item">MARLA BENNICK</li>
        <li class="artists__item">ROSALIND METCALF</li>
        <li class="artists__item">LYNETTE PAULSEN</li>
      </ul>

      <div class="brand brand--back">
        <span class="brand__dot"></span>
        <span class="brand__name">QUIMBY</span>
      </div>

      <address class="contact">
        Quimby Gallery &nbsp;2813 E<br>
        Fernwood Ave Yakima WA 98907<br>
        (509) 555-0193
      </address>
    </div>
  </section>
</main>
</body>
</html>
```